Cork Lantern website design elements

Company: Cork Lantern
Business: Wine website (selling wine online)
www.corklantern-demo.com.au
Please note that this is an initial project, ongoing design work will be required after this project.
Design requirement
Note: Full website design not required, only specific elements to enhance current design.
- Must work with existing logo and wood background (do not change site background)
- Must work with a orange (please improve current orange colour) and blue colour (blue colour in attachments)
- Pictures of wine bottles or wine glasses are not to be used in design elements.
I currently have an existing design which I would like certain elements designed for. Design elements must work with responsive functionality.
I am trying to achieve a modern retro feel of the website, please refer to the below websites as examples that I am trying to look like.
- https://au.brisktrimhouse-demo.com/
- http://www.kestrelmarlow-demo.com/italian/australia/home
- http://www.tangerinefizz-demo.co.uk/
- http://www.codeharbour-demo.org.nz/13/
As mentioned the site is already built and I need certain elements to work with what is already there. All elements must work with current logo and wood panel background.
I require the following elements
• Menu bar (must be the orange)
• Home page promo slider (Text, this weeks special etc)
• 2x homepage promo tabs buttons (Join the lantern club, what's in the box deal)
• 4x Homepage navigation tabs (Red wine, White wine, Sparkling, Pre mixed cases)
• Add to cart button
• Product image backdrop (can be wider than current examples)
o I would like the backdrops to be a different colour scheme to each other e.g red wine will habe red colour, white will have a cream colour, etc)
o I would prefer a close up of the product, does not need to be full view
Please refer to attachments for elements that I like and would like to mimic.
Colour scheme
- Use existing orange (please suggest if you think of a better tone)
- Secondary colour light baby blue (suggest best options)
- Please advise of other colours needed
Design elements to be provided in jog and raw design format.
This project will require ongoing work.
I will provide access details to site upon request.
Please contact me if you have any questions.
Tobias
Cork Lantern

```html
<!DOCTYPE html>
<html lang="en">
<head>
<meta charset="utf-8">
<title>Cork Lantern – Home</title>
<link href="https://fonts.googleapis.com/css2?family=Oswald:wght@400;500;700&family=Open+Sans:wght@400;600;700&family=Rokkitt:wght@400;700&display=swap" rel="stylesheet">
<style>
:root{
  --wood-dark:#6b4325;
  --wood-mid:#8d5d35;
  --wood-light:#a06c40;
  --orange:#ea6a26;
  --orange-dark:#c2501a;
  --blue:#86c8de;
  --blue-light:#cde9f2;
  --blue-deep:#3f8fb0;
  --navy:#2e5f78;
  --paper:#f5f1e8;
  --ink:#4a4a4a;
  --footer:#2e2e2e;
  --footer-dark:#232323;
  --footer-text:#bdbdbd;
  --white:#ffffff;
}
*{box-sizing:border-box;margin:0;padding:0}
html,body{width:855px;height:1200px;overflow:hidden}
body{position:relative;font-family:"Open Sans",Arial,sans-serif;color:var(--ink);background:var(--wood-mid)}
.abs{position:absolute}

/* site backdrop */
.backdrop{left:0;top:0;width:855px;height:940px;background:radial-gradient(ellipse at 50% 30%,var(--wood-light),var(--wood-mid) 55%,var(--wood-dark))}

/* header */
.brand{left:88px;top:26px;display:flex;align-items:center;gap:10px}
.brand-dot{width:70px;height:70px;border-radius:50%;background:var(--paper)}
.brand-name{font-family:"Oswald",sans-serif;font-weight:500;font-size:28px;color:var(--paper);letter-spacing:1px}
.search{left:455px;top:52px;width:262px;height:28px;background:var(--paper);border-radius:3px;display:flex;align-items:center;padding:0 10px;font-family:"Oswald",sans-serif;font-size:13px;color:#777;letter-spacing:1px}
.search svg{margin-left:auto}
.cart-btn{left:735px;top:38px;width:88px;height:70px;background:var(--orange);border:3px solid var(--paper);border-radius:6px;color:var(--white);font-family:"Oswald",sans-serif;font-size:13px;text-align:center;display:flex;flex-direction:column;align-items:center;justify-content:center;gap:4px}

/* nav */
.nav{left:100px;top:108px;width:725px;height:36px;background:var(--orange);display:flex;align-items:center;box-shadow:0 3px 0 var(--orange-dark)}
.nav a{font-family:"Oswald",sans-serif;color:var(--white);text-decoration:none;font-size:15px;padding:0 22px;height:100%;display:flex;align-items:center}
.nav a.active{background:var(--blue);color:var(--navy)}
.nav-fold{top:144px;width:0;height:0}
.fold-l{left:100px;border-top:10px solid var(--orange-dark);border-left:14px solid transparent}
.fold-r{left:811px;border-top:10px solid var(--orange-dark);border-right:14px solid transparent}

/* slider */
.slider{left:115px;top:160px;width:695px;height:240px;background:var(--blue);border-radius:10px;padding:10px}
.slide{width:100%;height:100%;border-radius:6px;background:radial-gradient(ellipse at 40% 40%,#4a4f52,#1f2224 75%);position:relative;overflow:hidden}
.slide-visual{position:absolute;left:30px;top:20px;width:200px;height:180px;border-radius:6px;background:radial-gradient(circle at 50% 50%,#5d6468,#2a2d2f 70%)}
.slide-title{position:absolute;left:250px;top:40px;width:400px;font-family:"Oswald",sans-serif;font-weight:700;color:var(--white);font-size:58px;line-height:1.1;text-align:center;text-transform:uppercase}
.slide-arrow{position:absolute;top:95px;width:26px;height:26px;border-radius:50%;background:rgba(255,255,255,.25)}
.slide-dots{position:absolute;bottom:8px;left:50%;transform:translateX(-50%);display:flex;gap:6px}
.slide-dots i{width:8px;height:8px;border-radius:50%;background:#888}
.slide-dots i.on{background:var(--orange)}

/* content */
.content{left:115px;top:400px;width:695px;height:540px;background:var(--paper)}
.welcome{position:absolute;left:0;top:40px;width:100%;text-align:center;font-family:"Rokkitt",serif;font-size:18px;color:#555}
.welcome b{color:var(--orange);font-weight:700;font-size:20px}
.intro{position:absolute;left:30px;top:72px;width:635px;font-size:9.5px;line-height:1.5;text-align:center;color:#777}
.btn{display:inline-block;background:var(--orange);color:var(--white);font-family:"Oswald",sans-serif;font-size:11px;padding:3px 12px;border-radius:3px}
.intro-btn{position:absolute;left:314px;top:160px}

.cards{position:absolute;left:20px;top:205px;width:655px;display:flex;justify-content:space-between}
.card{width:154px;height:150px;background:var(--blue-light);border:2px solid var(--blue);border-radius:6px;position:relative;padding:8px}
.card-tag{position:absolute;top:-12px;right:12px;width:30px;height:24px;background:var(--orange);clip-path:polygon(0 0,100% 0,100% 100%,50% 75%,0 100%)}
.card h3{font-family:"Oswald",sans-serif;font-weight:500;font-size:16px;color:var(--orange-dark)}
.card-media{position:absolute;left:8px;top:40px;width:44px;height:95px;border-radius:4px}
.media-red{background:linear-gradient(#f4eef0,#c7a2a9)}
.media-white{background:linear-gradient(#fbf8ef,#e6dcc0)}
.media-spark{background:linear-gradient(#fbf6e4,#e3cf8f)}
.media-mixed{background:linear-gradient(#f3ece2,#c9ad8c)}
.card p{position:absolute;left:58px;top:42px;width:84px;font-size:7.5px;line-height:1.45;color:#666}
.card .btn{position:absolute;left:62px;bottom:12px;font-size:10px;padding:3px 10px}

.promos{position:absolute;left:30px;top:365px;width:635px;display:flex;justify-content:space-between}
.promo{width:305px;height:160px;background:var(--blue-light);border:2px solid var(--blue);border-radius:6px;position:relative}
.promo h3{margin:10px auto 0;width:200px;background:var(--navy);color:var(--white);font-family:"Oswald",sans-serif;font-weight:500;font-size:15px;text-align:center;padding:4px 0;clip-path:polygon(0 0,100% 0,94% 50%,100% 100%,0 100%,6% 50%)}
.promo-icon{position:absolute;left:18px;top:55px;width:80px;height:80px;border-radius:50%;background:radial-gradient(circle,#ffffff,var(--blue))}
.promo p{position:absolute;left:112px;top:52px;width:178px;font-size:8.5px;line-height:1.5;color:#666}
.promo .btn{position:absolute;left:150px;bottom:14px}

/* notice band */
.notice{left:0;top:940px;width:855px;height:45px;background:var(--orange);color:var(--white);font-family:"Oswald",sans-serif;font-size:17px;letter-spacing:.5px;display:flex;align-items:center;justify-content:center}

/* footer */
.footer{left:0;top:985px;width:855px;height:185px;background:var(--footer);color:var(--footer-text);font-size:9px}
.f-col h4{font-family:"Oswald",sans-serif;font-weight:500;color:var(--white);font-size:13px;margin-bottom:8px}
.f-features{position:absolute;left:40px;top:18px}
.f-features li{list-style:none;line-height:1.75}
.f-suggest{position:absolute;left:220px;top:18px;width:250px}
.f-suggest li{list-style:none;display:flex;gap:8px;align-items:flex-start;margin-bottom:7px;line-height:1.35}
.f-suggest li i{flex:none;width:18px;height:18px;border-radius:3px;background:var(--blue-deep)}
.social{position:absolute;left:640px;top:18px;display:flex;gap:6px}
.social i{width:22px;height:22px;border-radius:50%;background:#555}
.f-contact{position:absolute;left:600px;top:58px;display:flex;gap:10px}
.f-logo{width:58px;height:58px;border-radius:50%;background:var(--paper);flex:none}
.f-contact p{line-height:1.6}
.f-contact b{color:var(--white);font-family:"Oswald",sans-serif;font-weight:500;font-size:11px}
.bottom{left:0;top:1170px;width:855px;height:30px;background:var(--footer-dark);color:#9a9a9a;font-size:8.5px;display:flex;align-items:center;justify-content:space-between;padding:0 40px}
</style>
</head>
<body>

<div class="abs backdrop" role="img" aria-label="Warm wood panel site background"></div>

<header>
  <div class="abs brand"><span class="brand-dot"></span><span class="brand-name">Cork Lantern</span></div>
  <div class="abs search">SEARCH
    <svg width="14" height="14" viewBox="0 0 14 14"><circle cx="6" cy="6" r="4.2" fill="none" stroke="#777" stroke-width="1.6"/><line x1="9" y1="9" x2="13" y2="13" stroke="#777" stroke-width="1.8"/></svg>
  </div>
  <div class="abs cart-btn">
    <svg width="22" height="18" viewBox="0 0 22 18"><path d="M1 2h4l3 10h10l2-7H6" fill="none" stroke="#fff" stroke-width="1.8"/><circle cx="9" cy="15.5" r="1.6" fill="#fff"/><circle cx="16" cy="15.5" r="1.6" fill="#fff"/></svg>
    ADD TO CART
  </div>
</header>

<nav class="abs nav">
  <a class="active" href="#">Home</a>
  <a href="#">Red wine</a>
  <a href="#">White wine</a>
  <a href="#">Sparkling</a>
  <a href="#">Mixed cases</a>
</nav>
<div class="abs nav-fold fold-l"></div>
<div class="abs nav-fold fold-r"></div>

<section class="abs slider">
  <div class="slide">
    <div class="slide-visual" role="img" aria-label="Featured wine close-up for this week's special"></div>
    <h1 class="slide-title">This weeks special etc</h1>
    <span class="slide-arrow" style="left:8px"></span>
    <span class="slide-arrow" style="right:8px"></span>
    <div class="slide-dots"><i class="on"></i><i></i><i></i><i></i></div>
  </div>
</section>

<main class="abs content">
  <h2 class="welcome">Welcome to <b>Cork Lantern</b></h2>
  <p class="intro">Lorem ipsum dolor sit amet, consectetuer adipiscing elit, sed diam nonummy nibh euismod tincidunt ut laoreet dolore magna aliquam erat volutpat. Ut wisi enim ad minim veniam, quis nostrud exerci tation ullamcorper suscipit lobortis nisl ut aliquip ex ea commodo consequat. Duis autem vel eum iriure dolor in hendrerit in vulputate velit esse molestie consequat, vel illum dolore eu feugiat nulla facilisis at vero eros et accumsan et iusto odio dignissim qui blandit praesent luptatum zzril delenit augue duis dolore te feugait nulla facilisi.</p>
  <span class="btn intro-btn">Read More</span>

  <div class="cards">
    <article class="card"><span class="card-tag"></span><h3>Red Wine</h3>
      <div class="card-media media-red" role="img" aria-label="Red wine product backdrop"></div>
      <p>Lorem ipsum dolor sit amet, consectetuer adipiscing elit, sed diam nonummy nibh euismod.</p>
      <span class="btn">Read More</span></article>
    <article class="card"><span class="card-tag"></span><h3>White Wine</h3>
      <div class="card-media media-white" role="img" aria-label="White wine product backdrop"></div>
      <p>Lorem ipsum dolor sit amet, consectetuer adipiscing elit, sed diam nonummy nibh euismod.</p>
      <span class="btn">Read More</span></article>
    <article class="card"><span class="card-tag"></span><h3>Sparkling</h3>
      <div class="card-media media-spark" role="img" aria-label="Sparkling wine product backdrop"></div>
      <p>Lorem ipsum dolor sit amet, consectetuer adipiscing elit, sed diam nonummy nibh euismod.</p>
      <span class="btn">Read More</span></article>
    <article class="card"><span class="card-tag"></span><h3>Mixed Cases</h3>
      <div class="card-media media-mixed" role="img" aria-label="Pre mixed case product backdrop"></div>
      <p>Lorem ipsum dolor sit amet, consectetuer adipiscing elit, sed diam nonummy nibh euismod.</p>
      <span class="btn">Read More</span></article>
  </div>

  <div class="promos">
    <article class="promo"><h3>Join The Lantern Club</h3>
      <div class="promo-icon" role="img" aria-label="Club membership illustration"></div>
      <p>Lorem ipsum dolor sit amet, consectetuer adipiscing elit, sed diam nonummy nibh euismod tincidunt ut laoreet dolore magna aliquam erat volutpat.</p>
      <span class="btn">Read More</span></article>
    <article class="promo"><h3>What In the Box?</h3>
      <div class="promo-icon" role="img" aria-label="Mixed case box illustration"></div>
      <p>Lorem ipsum dolor sit amet, consectetuer adipiscing elit, sed diam nonummy nibh euismod tincidunt ut laoreet dolore magna aliquam erat volutpat.</p>
      <span class="btn">Read More</span></article>
  </div>
</main>

<div class="abs notice">IT IS AN OFFENCE TO SUPPLY ALCOHOL TO A PERSON UNDER THE AGE OF 18 YEARS PENALTIES APPLY</div>

<footer class="abs footer">
  <div class="f-col f-features"><h4>Theme Features</h4>
    <ul><li>Theme Features</li><li>Typography</li><li>Sample Link</li><li>Meet Our Wine Partners</li><li>Our Other Projects</li><li>Find Out To Join Us</li><li>Seasonal Themes</li></ul>
  </div>
  <div class="f-col f-suggest"><h4>Tobias to Suggest</h4>
    <ul>
      <li><i></i>Unlimited colors, dozens of customizable elements. Sample text.</li>
      <li><i></i>Customizable navigation layouts based on fluid grid. Sample text.</li>
      <li><i></i>Six placeholders to display custom content. Sample text.</li>
      <li><i></i>Create your custom slide show. Sample text.</li>
    </ul>
  </div>
  <div class="social"><i></i><i></i><i></i><i></i><i></i><i></i></div>
  <div class="f-contact">
    <span class="f-logo"></span>
    <p><b>Cork Lantern</b> · (03) 9000 1234<br>12 Barrel Lane, Vintner VIC 3000<br>Open Mon–Fri 9am–5pm<br>hello@corklantern-demo.com.au<br>www.corklantern-demo.com.au</p>
  </div>
</footer>

<div class="abs bottom">
  <span>About Us &nbsp;|&nbsp; Shipping and Delivery &nbsp;|&nbsp; Refund Policy &nbsp;|&nbsp; Customer Service</span>
  <span>© 2013 Cork Lantern. All Rights Reserved.</span>
</div>

</body>
</html>
```